TRV Advisory Business Cards

Hi there,

I'd like to make a simple new business card design with the logo we already have created for our business.

I need a double sided business card with our logo on the front side and the company and person's details on the back side.

I'd like it to be on a white background and no background so I can potentially use it with either white paper or put it on different coloured paper in accordance with our business colours.

Please use the logo images I have attached and also the fonts.

So Front side:
- Logo in centre of business card (use medium logo so there is a pretty decent border around it, so don't want to fill the whole card but to make it prominent).

Back Side.
- We need 3 different business cards with the different people's name on each.

ie.

Dariel Moratkin
Business Development Manager

m +61 437 290 618
e dariel@trvadvisory.com.au
w trvadvisory.com.au

- Also I'd like to put only the cog/power button logo in the top right hand corner of the card.
(You might need to chop the current logo in half as I don't have a seperate log just for this)
- Also I'd like some lines running on the top left hand corner diagonally, anything that will add to the design or some swirling lines that add some cool effect to the card.

Also I'd like to maybe put our ABN in the bottom right hand corner of the card in a smaller font.

I'd like to also talk to the designer if possible so I can get my idea across a bit better.

Thanks!

Regards,
Dariel

```html
<!DOCTYPE html>
<html lang="en">
<head>
<meta charset="utf-8">
<title>TRV Advisory Business Cards</title>
<link href="https://fonts.googleapis.com/css2?family=Jost:wght@500&family=Michroma&display=swap" rel="stylesheet">
<style>
  :root {
    --bg: #e6e4e0;
    --card: #ffffff;
    --ink: #1f1f1f;
    --brand-orange: #f39322;
    --brand-grey: #4a4a4a;
    --brand-sand: #cfc9b0;
    --card-shadow: rgba(0, 0, 0, 0.18);
  }
  * { box-sizing: border-box; margin: 0; padding: 0; }
  html, body {
    width: 1200px;
    height: 900px;
    overflow: hidden;
    background: var(--bg);
  }
  .sheet {
    width: 1200px;
    height: 900px;
    display: flex;
    align-items: center;
    justify-content: center;
    gap: 40px;
  }
  .card {
    position: relative;
    width: 540px;
    height: 320px;
    background: var(--card);
    box-shadow: 0 6px 20px var(--card-shadow);
    overflow: hidden;
  }

  /* Front */
  .card-front {
    display: flex;
    align-items: center;
    justify-content: center;
  }
  .brand-lockup {
    display: flex;
    align-items: center;
    gap: 14px;
  }
  .brand-dot {
    width: 46px;
    height: 46px;
    border-radius: 50%;
    background: var(--brand-grey);
  }
  .brand-name {
    font-family: "Jost", sans-serif;
    font-size: 44px;
    font-weight: 500;
    color: var(--brand-orange);
  }

  /* Back */
  .corner-decoration {
    position: absolute;
    top: 0;
    left: 0;
    width: 140px;
    height: 140px;
    clip-path: polygon(0 0, 100% 0, 0 100%);
    background: linear-gradient(135deg, var(--brand-orange) 0%, var(--brand-grey) 60%, var(--brand-sand) 100%);
  }
  .corner-brand {
    position: absolute;
    top: 22px;
    right: 22px;
    display: flex;
    align-items: center;
    gap: 8px;
  }
  .corner-brand .brand-dot {
    width: 22px;
    height: 22px;
  }
  .corner-brand .brand-name {
    font-size: 17px;
  }
  .person {
    position: absolute;
    top: 104px;
    left: 40px;
    right: 20px;
    text-align: center;
    color: var(--ink);
  }
  .person-name {
    font-family: "Jost", sans-serif;
    font-size: 34px;
    font-weight: 500;
    letter-spacing: 0.3px;
  }
  .person-role {
    margin-top: 6px;
    font-family: "Michroma", sans-serif;
    font-size: 13px;
    font-variant: small-caps;
    letter-spacing: 2.4px;
  }
  .contact {
    position: absolute;
    left: 30px;
    bottom: 26px;
    list-style: none;
    font-family: "Michroma", sans-serif;
    font-size: 11px;
    font-variant: small-caps;
    letter-spacing: 1.6px;
    line-height: 22px;
    color: var(--ink);
  }
  .contact-label { margin-right: 6px; }
  .abn {
    position: absolute;
    right: 28px;
    bottom: 74px;
    font-family: "Michroma", sans-serif;
    font-size: 9px;
    letter-spacing: 1.4px;
    color: var(--ink);
  }
</style>
</head>
<body>
<main class="sheet">
  <section class="card card-front" aria-label="Card front">
    <div class="brand-lockup">
      <span class="brand-dot"></span>
      <span class="brand-name">TRV Advisory</span>
    </div>
  </section>

  <section class="card card-back" aria-label="Card back">
    <div class="corner-decoration" role="img" aria-label="Diagonal stripe decoration in orange, grey and sand"></div>

    <div class="corner-brand">
      <span class="brand-dot"></span>
      <span class="brand-name">TRV Advisory</span>
    </div>

    <div class="person">
      <h1 class="person-name">Dariel Moratkin</h1>
      <p class="person-role">Business Development Manager</p>
    </div>

    <ul class="contact">
      <li><span class="contact-label">m</span>+61 437 290 618</li>
      <li><span class="contact-label">e</span>dariel@trvadvisory.com.au</li>
      <li><span class="contact-label">w</span>trvadvisory.com.au</li>
    </ul>

    <p class="abn">ABN: 4720 1938 065</p>
  </section>
</main>
</body>
</html>
```